Silver Birch Decorators Banner

Create a banner that displays and reinforces Silver Birch Decorators’ brand identity while promoting our interior painting services. The banner will be displayed at indoor venues through the winter. The design should be clean, professional, and visually recognizable to both new and returning customers. See attached design brief & logo source files.

```html
<!DOCTYPE html>
<html lang="en">
<head>
<meta charset="utf-8">
<title>Silver Birch Decorators – Interior Painting Banner</title>
<link rel="stylesheet" href="https://fonts.googleapis.com/css2?family=League+Gothic&family=Montserrat:wght@700;800&family=Roboto:wght@500&display=swap">
<style>
  :root {
    --stage: #9a9a9a;
    --paper-top: #e9e9e9;
    --paper-bottom: #ffffff;
    --charcoal: #484746;
    --leaf: #769a5c;
    --white: #ffffff;
  }
  * { margin: 0; padding: 0; box-sizing: border-box; }
  html, body {
    width: 1200px;
    height: 651px;
    overflow: hidden;
    background: var(--stage);
  }
  .banner {
    position: absolute;
    left: 20px;
    top: 93px;
    width: 1160px;
    height: 464px;
    overflow: hidden;
    background: linear-gradient(160deg, var(--paper-top) 0%, var(--paper-bottom) 60%);
  }
  .banner-shapes {
    position: absolute;
    inset: 0;
    width: 100%;
    height: 100%;
  }
  .brand-name {
    position: absolute;
    left: 47px;
    top: 44px;
    font-family: "Montserrat", sans-serif;
    font-weight: 800;
    font-size: 33px;
    line-height: 34px;
    color: var(--leaf);
    letter-spacing: 0.5px;
  }
  .headline {
    position: absolute;
    left: 46px;
    top: 156px;
    font-family: "Montserrat", sans-serif;
    font-weight: 800;
    color: var(--charcoal);
    line-height: 1;
  }
  .headline-line { display: block; }
  .headline-line--lead { font-size: 43px; }
  .headline-line--accent { font-size: 43px; color: var(--leaf); margin-top: 5px; }
  .headline-line--year { font-size: 60px; margin-top: 3px; }
  .cta {
    position: absolute;
    left: 90px;
    top: 366px;
    width: 430px;
    text-align: center;
    color: var(--white);
  }
  .cta-lead {
    font-family: "League Gothic", sans-serif;
    font-size: 33px;
    line-height: 34px;
    letter-spacing: 0.3px;
  }
  .cta-url {
    font-family: "Montserrat", sans-serif;
    font-weight: 700;
    font-size: 30px;
    line-height: 34px;
  }
  .services-title {
    position: absolute;
    left: 632px;
    top: 49px;
    width: 528px;
    height: 60px;
    background: var(--white);
    border-radius: 30px 0 0 30px;
    padding-left: 28px;
    font-family: "League Gothic", sans-serif;
    font-size: 60px;
    line-height: 62px;
    color: var(--leaf);
    letter-spacing: 0.2px;
    white-space: nowrap;
  }
  .services-list {
    position: absolute;
    left: 715px;
    top: 114px;
    list-style: none;
    font-family: "Roboto", sans-serif;
    font-weight: 500;
    font-size: 39px;
    line-height: 58.5px;
    color: var(--white);
  }
</style>
</head>
<body>
  <main class="banner">
    <svg class="banner-shapes" viewBox="0 0 1160 464" preserveAspectRatio="none" aria-hidden="true">
      <path class="cta-band" fill="#484746"
        d="M0 343 C20 338 40 340 60 352 C80 362 100 362 120 352 C140 340 170 338 190 350 C210 362 235 362 255 350 C275 338 305 338 325 352 C345 362 370 362 390 350 C410 338 440 338 460 350 C480 362 505 362 525 352 C545 340 575 338 595 350 C615 362 640 360 660 354 L660 464 L0 464 Z"/>
      <path class="service-panel" fill="#769a5c"
        d="M655 0 L1160 0 L1160 464 L630 464 L626 452 L636 446 L620 440 L632 432 L618 424 L630 418 L614 410 L628 402 L616 396 L632 386 L622 378 L640 370 L630 362 L650 352 L642 344 L662 334 L652 326 L674 316 L664 306 L680 298 L668 290 L676 280 L660 272 L670 264 L652 256 L664 248 L646 240 L656 232 L638 224 L650 216 L632 208 L646 200 L628 192 L640 184 L620 176 L632 168 L614 160 L626 152 L606 146 L622 138 L602 130 L616 122 L598 114 L612 106 L594 98 L606 90 L590 82 L604 74 L594 64 L612 56 L604 48 L624 38 L616 30 L638 20 L630 12 Z"/>
      <path class="panel-notch" fill="#484746" d="M786 464 L845 412 L866 464 Z"/>
    </svg>

    <div class="brand-name">SILVER BIRCH<br>DECORATORS</div>

    <h1 class="headline">
      <span class="headline-line headline-line--lead">TRUSTED LOCAL</span>
      <span class="headline-line headline-line--accent">PROFESSIONALS,</span>
      <span class="headline-line headline-line--year">SINCE 2005</span>
    </h1>

    <div class="cta">
      <p class="cta-lead">Book a Free Estimate at</p>
      <p class="cta-url">www.silverbirchdecor.com</p>
    </div>

    <h2 class="services-title">INTERIOR PAINTING SERVICES</h2>
    <ul class="services-list">
      <li>Walls</li>
      <li>Ceilings</li>
      <li>Trim</li>
      <li>Cabinets</li>
      <li>Drywall Repair</li>
    </ul>
  </main>
</body>
</html>
```